Tovex - Business Card Design

Design a modern masculine business card for our business

Target Market(s)

Private Market

Industry/Entity Type

Construction

Contact Information for Business Card

Company Name - Name of Person - Address - email address - contact number

Font styles to use
Serif
Sans Serif

Colors
0094D4
00A9DD
6FCCEA
C7EBF8
E9F6FB
00AB8E
00BBA5
67D7C9
C6EFE9
E9F9F6
F0912C
F2A743
F7CA91
FBE8D2
FDF5EE

Requirements
Must have
• Use company logo provided
Nice to have
• Company Logo

```html
<!DOCTYPE html>
<html lang="en">
<head>
<meta charset="utf-8">
<title>Tovex Construction – Business Card</title>
<link href="https://fonts.googleapis.com/css2?family=Montserrat:wght@400;700;800&display=swap" rel="stylesheet">
<style>
  :root {
    --backdrop: #161616;
    --card: #262626;
    --orange: #f26f22;
    --white: #ffffff;
    --muted: #e6e6e6;
  }
  * { box-sizing: border-box; margin: 0; padding: 0; }
  html, body {
    width: 1200px; height: 900px; overflow: hidden;
    background: var(--backdrop);
    font-family: "Montserrat", Arial, sans-serif;
  }
  .card {
    position: absolute; left: 75px; top: 150px;
    width: 1050px; height: 600px;
    background: var(--card);
    overflow: hidden;
  }
  .brand {
    position: absolute; left: 400px; top: 120px;
    display: flex; align-items: center; gap: 22px;
  }
  .brand-square {
    width: 44px; height: 44px; background: var(--orange);
  }
  .brand-name {
    color: var(--white); font-weight: 800; font-size: 96px;
    letter-spacing: 2px; line-height: 1; text-transform: uppercase;
  }
  .brand-sub {
    position: absolute; left: 470px; top: 232px;
    color: var(--white); font-weight: 800; font-size: 22px;
    letter-spacing: 4px; text-transform: uppercase;
  }
  .person {
    position: absolute; right: 610px; top: 330px; text-align: right;
  }
  .person-name {
    color: var(--orange); font-weight: 800; font-size: 34px;
    text-transform: uppercase; letter-spacing: 1px;
  }
  .person-title {
    color: var(--muted); font-weight: 400; font-size: 25px; margin-top: 4px;
  }
  .divider {
    position: absolute; left: 480px; top: 315px;
    width: 2px; height: 190px; background: var(--orange);
  }
  .contact {
    position: absolute; left: 515px; top: 318px;
    color: var(--white); font-size: 24px; line-height: 1.3;
    list-style: none;
  }
  .contact li { display: flex; align-items: center; gap: 12px; }
  .contact .address { padding-left: 36px; }
  .contact svg { width: 24px; height: 24px; flex: none; }
  .edge-band {
    position: absolute; left: 0; bottom: 0; width: 100%; height: 12px;
    background: var(--orange);
  }
</style>
</head>
<body>
  <section class="card">
    <div class="brand">
      <span class="brand-square"></span>
      <span class="brand-name">Tovex</span>
    </div>
    <div class="brand-sub">Construction, Inc</div>

    <div class="person">
      <h1 class="person-name">Dalen Marsh</h1>
      <p class="person-title">CEO/Founder</p>
    </div>

    <span class="divider"></span>

    <ul class="contact">
      <li class="address">8542 Street Name</li>
      <li class="address">Country Name AB 8542</li>
      <li>
        <svg viewBox="0 0 24 24" aria-hidden="true"><path fill="#f26f22" d="M6.6 10.8a15 15 0 0 0 6.6 6.6l2.2-2.2c.3-.3.7-.4 1-.2 1.1.4 2.3.6 3.6.6.6 0 1 .4 1 1V20c0 .6-.4 1-1 1A17 17 0 0 1 3 4c0-.6.4-1 1-1h3.5c.6 0 1 .4 1 1 0 1.3.2 2.5.6 3.6.1.3 0 .7-.2 1z"/></svg>
        123.456.7890
      </li>
      <li>
        <svg viewBox="0 0 24 24" aria-hidden="true"><rect x="2" y="5" width="20" height="14" fill="#f26f22"/><path d="M2 5l10 8 10-8" fill="none" stroke="#262626" stroke-width="2"/></svg>
        info@tovexbuild.com
      </li>
      <li>
        <svg viewBox="0 0 24 24" aria-hidden="true"><circle cx="12" cy="12" r="10" fill="#f26f22"/><path d="M2 12h20M12 2c3 3 3 17 0 20M12 2c-3 3-3 17 0 20" fill="none" stroke="#262626" stroke-width="1.5"/></svg>
        www.tovexbuild.com
      </li>
    </ul>

    <div class="edge-band"></div>
  </section>
</body>
</html>
```